Telecom Services Corporate Webpage

Design a modern HTML5 website for the company that promotes its communications services and rentals. Cell towers, drilling rigs, and satellite systems would make for good imagery.

Contact me for competitor website links to draw some comparisons.

[Pages Required]
'INDEX' page with large background graphic. Flashy show page to summarize what we do.

'COMPANY' page. Various information about the company.

'CAREERS' page. Self explanatory.

'PRODUCTS & SERVICES' page. Will give a brief description about our various products and services we offer.

'HSE' page. Will have information about our Health, Safety, and Environmental standards.

'CONTACT US' page. Self explanatory.

Existing and potential customers of telecommunications services and rentals including Oil & Gas companies, remote man camps, telecom carriers, government, etc.

Telecommunications

Coded - Design and coding required

5+ page

Designer to choose colors to be used in the design.

• Fully working top menu bar with sub items.

```html
<!DOCTYPE html>
<html lang="en">
<head>
<meta charset="utf-8">
<title>Northlink Communications</title>
<link href="https://fonts.googleapis.com/css2?family=Montserrat:wght@300;400;500;600;700&display=swap" rel="stylesheet">
<style>
:root{
  --olive:#625a2b;
  --olive-dark:#4f4822;
  --ink:#1c1c1c;
  --text:#3d3d3d;
  --card-label:#ebe9e3;
  --white:#ffffff;
  --black:#000000;
  --hero-top:#4d63ad;
  --hero-mid:#8e86c2;
  --hero-low:#e7a6b9;
}
*{box-sizing:border-box;margin:0;padding:0}
html,body{width:1200px;height:2267px;overflow:hidden}
body{position:relative;background:var(--white);font-family:"Montserrat",sans-serif;color:var(--text)}
.abs{position:absolute}

/* header */
.brand{left:100px;top:22px;display:flex;align-items:center;gap:12px}
.brand-dot{width:40px;height:40px;border-radius:50%;background:var(--olive)}
.brand-name{font-size:34px;font-weight:700;color:var(--olive);letter-spacing:1px}
.top-contacts{right:112px;top:34px;display:flex;align-items:center;gap:34px;white-space:nowrap}
.top-contact{font-size:14px;color:var(--ink);display:flex;align-items:center;gap:10px}
.top-contact svg{fill:var(--ink);flex:none}

/* nav */
.nav{left:0;top:92px;width:1200px;height:55px;background:var(--olive)}
.nav ul{list-style:none;display:flex;position:absolute;left:99px;top:0;height:55px}
.nav li{height:55px;line-height:55px;padding:0 21px;color:var(--white);font-size:14.5px;font-weight:600;text-transform:uppercase}
.nav li.active{background:var(--olive-dark)}
.nav .search{position:absolute;left:1081px;top:19px}

/* hero */
.hero{left:0;top:147px;width:1200px;height:556px;
  background:linear-gradient(200deg,var(--hero-top) 0%,var(--hero-mid) 45%,var(--hero-low) 90%);
  clip-path:polygon(0 0,100% 0,100% 473px,0 556px)}
.hero-title{left:100px;top:240px;font-size:42px;line-height:48px;font-weight:700;color:var(--white);white-space:nowrap}
.hero-text{left:101px;top:352px;width:405px;font-size:16px;line-height:25.5px;color:var(--white)}
.hero-btn{left:101px;top:471px;width:176px;height:52px;background:var(--olive);color:var(--white);font-size:21px;display:flex;align-items:center;justify-content:center}
.hero-arrows{left:108px;top:564px}

/* welcome */
.welcome-mark{left:580px;top:717px;width:40px;height:40px;border-radius:50%;background:var(--olive)}
.section-title{left:0;width:1200px;text-align:center;font-size:20px;font-weight:700;color:var(--ink)}
.rule{height:3px;width:50px;background:var(--ink)}
.welcome-text{left:120px;top:834px;width:960px;text-align:center;font-size:14.5px;line-height:21.8px;color:var(--text)}
.btn-read{left:524px;top:938px;width:152px;height:50px;background:var(--olive);color:var(--white);font-size:15px;font-weight:600;display:flex;align-items:center;justify-content:center}

/* services */
.service{top:1085px;width:247px;height:328px}
.service-photo{height:252px}
.service-label{height:76px;display:flex;align-items:center;justify-content:center;font-size:21px;font-weight:600;color:var(--ink);background:var(--card-label);text-transform:uppercase}
.service.featured .service-label{background:var(--olive);color:var(--white)}

/* innovators */
.innov-title{left:98px;top:1484px;font-size:21px;line-height:33px;font-weight:700;color:var(--ink);white-space:nowrap}
.innov-list{list-style:none;top:1580px;font-size:15px;line-height:25.7px;color:var(--text);white-space:nowrap}
.innov-photo{left:610px;top:1455px;width:491px;height:354px;
  background:linear-gradient(180deg,#d9ccb2 0%,#cdb8a7 55%,#2f4a52 100%);
  box-shadow:0 2px 8px rgba(0,0,0,.35)}

/* partners */
.footer{left:0;top:1927px;width:1200px;height:340px;background:var(--black)}
.partners{left:116px;top:1881px;width:770px;height:83px;background:var(--white);display:flex;align-items:center;gap:38px;padding-left:75px}
.partner-badge{width:70px;height:22px;background:#b9b9b9;border-radius:3px}
.partners-tag{left:873px;top:1878px;width:212px;height:101px;background:var(--olive);clip-path:polygon(20% 0,100% 0,80% 100%,0 100%)}
.partners-tag span{position:absolute;left:0;width:212px;text-align:center;color:#e9e4cf;font-size:23px;font-weight:300;line-height:27px;top:22px}

/* footer */
.foot-head{top:2039px;font-size:17px;font-weight:700;color:var(--white);text-transform:uppercase}
.foot-links{list-style:none;top:2090px;font-size:12px;line-height:25.7px;color:var(--white)}
.foot-item{left:514px;font-size:12px;line-height:21px;color:var(--white);display:flex;gap:14px;white-space:nowrap}
.foot-item svg{fill:var(--white);flex:none;margin-top:4px}
.social{left:857px;top:2089px;display:flex;gap:16px}
.social span{width:16px;height:16px;border-radius:50%;background:var(--white)}
.foot-brand{left:857px;top:2142px;display:flex;align-items:center;gap:10px}
.foot-brand .brand-dot{width:40px;height:40px}
.foot-brand .brand-name{font-size:32px}
.copyright{left:866px;top:2205px;font-size:15px;color:var(--white);white-space:nowrap}
</style>
</head>
<body>

<header>
  <div class="abs brand"><span class="brand-dot"></span><span class="brand-name">NORTHLINK</span></div>
  <div class="abs top-contacts">
    <div class="top-contact">
      <svg width="14" height="11" viewBox="0 0 14 11"><path d="M0 0h14v1.5L7 6 0 1.5zM0 3l7 4.5L14 3v8H0z"/></svg>
      <span>Email Us :sales@northlinkcomms.ca</span>
    </div>
    <div class="top-contact">
      <svg width="14" height="14" viewBox="0 0 14 14"><path d="M3 0l2.5 3.5-1.6 1.6c.8 1.9 2.4 3.5 4.5 4.5l1.6-1.6L14 10.5 12.3 13.6C6 13 1 8 .4 1.7z"/></svg>
      <span>Call Us : 780-555-0142</span>
    </div>
  </div>
</header>

<nav class="abs nav">
  <ul>
    <li class="active">Home</li><li>About Us</li><li>Services</li><li>Features</li><li>Blog</li><li>Contact Us</li>
  </ul>
  <svg class="search" width="16" height="16" viewBox="0 0 16 16"><circle cx="6.5" cy="6.5" r="4.8" fill="none" stroke="#fff" stroke-width="2.2"/><path d="M10 10l4.5 4.5" stroke="#fff" stroke-width="2.6" stroke-linecap="round"/></svg>
</nav>

<section>
  <div class="abs hero" role="img" aria-label="Telecom tower with microwave dishes against a dusk sky"></div>
  <h1 class="abs hero-title">NORTHLINK<br>COMMUNICATIONS</h1>
  <p class="abs hero-text">Sed ut perspiciatis unde omnis iste natus error sit voluptatem accusantium doloremque laudantium, totam rem aperiam, eaque ipsa quia voluptas sit aspernatur aut odit aut fugit,</p>
  <div class="abs hero-btn">Learn More</div>
  <svg class="abs hero-arrows" width="110" height="62" viewBox="0 0 110 62"><path d="M30 1L1 31l29 30M80 1l29 30-29 30" fill="none" stroke="#fff" stroke-width="1.5"/></svg>
</section>

<section>
  <span class="abs welcome-mark"></span>
  <h2 class="abs section-title" style="top:776px">WELCOME TO NORTHLINK COMMUNICATIONS</h2>
  <div class="abs rule" style="left:575px;top:812px"></div>
  <p class="abs welcome-text">Sed ut perspiciatis unde omnis iste natus error sit voluptatem accusantium doloremque laudantium, totam rem aperiam, eaque ipsa quae ab illo inventore veritatis et quasi architecto beatae vitae dicta sunt explicabo. Nemo enim ipsam voluptatem quia voluptas sit aspernatur aut odit aut fugit, sed quia consequuntur magni dolores eos qui ratione voluptatem sequi nesciunt. Neque porro quisquam est, qui dolorem ipsum quia dolor sit amet, consectetur,</p>
  <div class="abs btn-read">READ MORE</div>
</section>

<section>
  <h2 class="abs section-title" style="top:1018px">SERVICES</h2>
  <div class="abs rule" style="left:575px;top:1053px"></div>
  <div class="abs service" style="left:98px">
    <div class="service-photo" role="img" aria-label="Offshore oil and gas drilling platform at sea" style="background:linear-gradient(180deg,#3a63b8 0%,#6f8fc6 60%,#1e3550 100%)"></div>
    <div class="service-label">Oil &amp; Gas</div>
  </div>
  <div class="abs service featured" style="left:351px">
    <div class="service-photo" role="img" aria-label="Workers welding a pipeline at a remote camp" style="background:linear-gradient(180deg,#8a6a52 0%,#6b5040 55%,#3d2f28 100%)"></div>
    <div class="service-label">Man Camps</div>
  </div>
  <div class="abs service" style="left:603px">
    <div class="service-photo" role="img" aria-label="Tall forest canopy seen from below" style="background:linear-gradient(180deg,#8fa27a 0%,#4c6a36 50%,#1e2b17 100%)"></div>
    <div class="service-label">Forestry</div>
  </div>
  <div class="abs service" style="left:855px">
    <div class="service-photo" role="img" aria-label="Telecom mast covered with antennas and dishes" style="background:linear-gradient(180deg,#a6b8cc 0%,#7c90a8 50%,#3e4c60 100%)"></div>
    <div class="service-label">Telecom</div>
  </div>
</section>

<section>
  <h2 class="abs innov-title">WESTERN CANADA'S<br>COMMUNICATIONS INNOVATORS</h2>
  <div class="abs rule" style="left:98px;top:1555px"></div>
  <ul class="abs innov-list" style="left:101px">
    <li>Tower Construction</li><li>Tower Maintenance</li><li>Portable Towers</li><li>Facility Cabling</li><li>Custom Installations</li><li>Remote Management</li><li>Distributed Antenna Systems</li><li>Surveillance Systems</li>
  </ul>
  <ul class="abs innov-list" style="left:341px">
    <li>LTE Repeaters</li><li>LTE Internet</li><li>Satellite Internet</li><li>Wi-Fi Distribution</li><li>VOIP Service</li><li>Wireless Intercoms</li><li>TV Head-End Systems</li><li>Radio Packages UHF/VHF</li>
  </ul>
  <div class="abs innov-photo" role="img" aria-label="Construction cranes silhouetted against a pale evening sky"></div>
</section>

<footer>
  <div class="abs footer"></div>
  <div class="abs partners">
    <span class="partner-badge"></span><span class="partner-badge"></span><span class="partner-badge"></span><span class="partner-badge"></span><span class="partner-badge" style="width:36px"></span><span class="partner-badge"></span>
  </div>
  <div class="abs partners-tag"><span>Our<br>Partners</span></div>

  <h3 class="abs foot-head" style="left:110px">Quick Links</h3>
  <ul class="abs foot-links" style="left:110px"><li>Home</li><li>About Us</li><li>Services</li><li>Blog</li></ul>
  <ul class="abs foot-links" style="left:273px"><li>News</li><li>Testimonials</li><li>Conact Us</li></ul>

  <h3 class="abs foot-head" style="left:505px">Contact Us</h3>
  <div class="abs foot-item" style="top:2090px">
    <svg width="10" height="13" viewBox="0 0 10 13"><path d="M5 0a5 5 0 0 1 5 5c0 3-5 8-5 8S0 8 0 5a5 5 0 0 1 5-5zm0 3a2 2 0 1 0 0 4 2 2 0 0 0 0-4z"/></svg>
    <span>Suite 210, 4500 - 52nd Avenue<br>Ridgeview, AB - T0H 2K0</span>
  </div>
  <div class="abs foot-item" style="top:2151px">
    <svg width="11" height="11" viewBox="0 0 14 14"><path d="M3 0l2.5 3.5-1.6 1.6c.8 1.9 2.4 3.5 4.5 4.5l1.6-1.6L14 10.5 12.3 13.6C6 13 1 8 .4 1.7z"/></svg>
    <span>780-555-0142</span>
  </div>
  <div class="abs foot-item" style="top:2192px">
    <svg width="12" height="9" viewBox="0 0 14 11"><path d="M0 0h14v1.5L7 6 0 1.5zM0 3l7 4.5L14 3v8H0z"/></svg>
    <span>sales@northlinkcomms.ca</span>
  </div>

  <h3 class="abs foot-head" style="left:857px">Follow Us</h3>
  <div class="abs social"><span></span><span></span><span></span><span></span></div>
  <div class="abs foot-brand"><span class="brand-dot"></span><span class="brand-name">NORTHLINK</span></div>
  <p class="abs copyright">© 2018 | www.companyname.com</p>
</footer>

</body>
</html>
```